Online Marketing Website

Create a website design for an online marketing company.

It should use modern designs:

Power of space,
Graphics supported content - less words more meaning
Grid and flow layout for listing type content
Provision for responsive and interactive CSS

http://www.bluelanternworks.com.au/ is a very quick mock up, however this should only be used as an example and is not a indication of desired design. Examples that differ from this will be considered.
Updates

To all the developers who have submitted a design, There are a lot a great designs there. I am going to wait a little while longer before providing any feedback as I do not like wasting your time, and experience has shown good designs come late.

At this stage no news is not bad news... It is just that.

Thanks heaps for your work, will contact the leaders soon.

Target Market(s)

Small to Medium Business operating in the B2B or professional B2C space

Industry/Entity Type

Marketing

Requirements
Must have
• It should use a modern Panel design for the front page that will give a high level overview of the products with in-depth content pages for each service.

Nice to have
• Rotating banner at the top of the pages, no higher than 300px

Appropriate use of power colours such as red and Orange.
Should not have
• No Sidebars except on Post pages

```html
<!DOCTYPE html>
<html lang="en">
<head>
<meta charset="utf-8">
<title>Blue Lantern Works – Online Strategic Planning</title>
<link href="https://fonts.googleapis.com/css2?family=Lato:ital,wght@0,300;0,400;0,700;1,700&display=swap" rel="stylesheet">
<style>
:root{
  --crimson:#c41e33;
  --orange:#e8731f;
  --amber:#f7b02a;
  --green:#5bbf21;
  --rust:#d9401a;
  --navy:#1a4f94;
  --sky:#74bdf0;
  --ink:#333333;
  --muted:#555555;
  --panel:#f4f4f4;
  --dark-btn:#4a4a4a;
  --white:#ffffff;
}
*{margin:0;padding:0;box-sizing:border-box}
html,body{width:753px;height:1200px;overflow:hidden;background:var(--white)}
body{position:relative;font-family:'Lato',Arial,sans-serif;color:var(--ink)}
.abs{position:absolute}
.rule-top,.rule-bottom{position:absolute;left:0;width:753px;height:2px;background:var(--crimson)}
.rule-top{top:0}.rule-bottom{top:1197px}
.page{position:absolute;left:62px;top:2px;width:628px;height:1130px;background:var(--panel)}
.brand{left:72px;top:16px;display:flex;align-items:center;gap:10px}
.brand-mark{width:30px;height:30px;background:var(--crimson)}
.brand-name{font-weight:700;font-size:17px;color:var(--crimson);line-height:1}
.nav{top:51px;left:460px;display:flex;gap:17px;font-size:10px;color:var(--ink)}
.banner{left:56px;top:78px;width:641px;height:188px;background:radial-gradient(ellipse at 70% 10%,#f7a51a 0%,#ef7d10 45%,#e5620a 100%)}
.banner-tab{position:absolute;top:-7px;width:0;height:0;border-bottom:7px solid #9c1424}
.banner-tab.left{left:0;border-left:7px solid transparent}
.banner-tab.right{right:0;border-right:7px solid transparent}
.banner-visual{left:16px;top:10px;width:230px;height:170px;border-radius:18px;background:linear-gradient(135deg,#f0f0f0 0%,#c41e33 50%,#3a3a3a 100%);opacity:.9}
.banner-title{left:280px;top:58px;font-weight:300;font-size:19px;color:var(--white);letter-spacing:.2px}
.banner-text{left:282px;top:90px;width:316px;font-size:8.6px;line-height:11.5px;color:var(--white)}
.banner-arrows{left:24px;top:165px;display:flex;gap:6px}
h2{position:absolute;font-weight:400;font-size:16.5px;color:var(--crimson);letter-spacing:.1px}
.lede{font-weight:700;font-style:italic;font-size:10px}
.copy{font-size:8.6px;line-height:11.5px;color:var(--ink)}
.stat{top:376px;width:139px;height:58px;color:var(--white);font-size:9.5px;text-align:center}
.stat-label{position:absolute;left:0;right:0;top:18px;line-height:12px}
.stat-label.single{top:24px}
.stat-bar{position:absolute;left:2px;bottom:2px;width:135px;height:10px;background:rgba(255,255,255,.35)}
.stat-fill{position:absolute;left:0;top:0;height:10px;background:var(--white)}
.stat-pct{position:absolute;right:5px;bottom:2px;font-size:9px;line-height:10px}
.stat.green{left:77px;background:var(--green)}
.stat.rust{left:230px;background:var(--rust)}
.stat.navy{left:384px;background:var(--navy)}
.stat.sky{left:536px;background:var(--sky)}
.stat-caption{top:452px;width:125px;font-size:9.5px;line-height:12px;text-align:center;color:var(--ink)}
.video{left:82px;top:627px;width:240px;height:140px;background:var(--white);border:1px solid #cfcfcf}
.video-art{position:absolute;left:50px;top:7px;width:136px;height:126px;border-radius:50%;background:radial-gradient(circle,#f6b08a 0%,#f0a07a 45%,#e6e6e6 75%,#f4f4f4 100%)}
.video-play{position:absolute;left:102px;top:53px}
.sells-text{left:358px;top:632px;width:272px;font-size:8.6px;line-height:15px}
.btn-more{left:358px;top:774px;width:56px;height:16px;background:#e5620a;color:var(--white);font-size:8.6px;line-height:16px;text-align:center}
.tab{top:809px;height:59px;color:var(--white);font-size:15px;font-weight:400;display:flex;align-items:center;padding-left:36px;line-height:16px}
.tab.plan{left:62px;width:209px;background:var(--crimson)}
.tab.packages{left:272px;width:208px;background:var(--orange);padding-left:26px}
.tab.articles{left:481px;width:209px;background:var(--amber);padding-left:24px}
.tab-pointer{left:91px;top:868px;border-left:7px solid transparent;border-right:7px solid transparent;border-top:7px solid var(--crimson)}
.plan-copy{left:85px;width:578px;font-size:8.6px;line-height:11px}
.day{top:1048px;height:22px;color:var(--white);font-size:9px;line-height:22px;text-align:center;background:var(--dark-btn);border:1px solid #333}
.day.active{background:var(--crimson);border-color:var(--crimson)}
.share{top:1092px;height:12px;display:flex;align-items:center;gap:3px;font-size:7px;color:#444}
.share-btn{border:1px solid #bbb;background:var(--white);padding:0 4px;line-height:10px;border-radius:2px}
.share-count{border:1px solid #ccc;padding:0 3px;line-height:10px;background:var(--white)}
.share-dot{width:8px;height:8px;border-radius:50%;background:#888}
.footer-nav{left:264px;top:1148px;display:flex;gap:12px;font-size:10px;color:#666}
.copyright{left:313px;top:1171px;font-size:8px;color:#666}
</style>
</head>
<body>
<div class="rule-top"></div>
<div class="page"></div>

<header>
  <div class="abs brand">
    <div class="brand-mark"></div>
    <div class="brand-name">BLUE LANTERN WORKS</div>
  </div>
  <nav class="abs nav"><span>STRATEGIC PLANNING</span><span>SEO</span><span>CONTACT</span></nav>
</header>

<section class="abs banner">
  <span class="banner-tab left"></span><span class="banner-tab right"></span>
  <div class="abs banner-visual" role="img" aria-label="Diamond collage of a businesswoman with SEO, Planning and Business labels"></div>
  <div class="abs banner-title">WHAT IS AN ONLINE STRATEGIC PLAN</div>
  <p class="abs banner-text">An Online Strategic Plan is a lot like a business plan. You define look at your business, define your values, look at your competitors and think and talk to your customers to determine what you should do to improve your current situation.</p>
  <div class="abs banner-arrows">
    <svg width="6" height="12" viewBox="0 0 6 12"><path d="M6 0L0 6l6 6z" fill="#fff"/></svg>
    <svg width="6" height="12" viewBox="0 0 6 12"><path d="M0 0l6 6-6 6z" fill="#fff"/></svg>
  </div>
</section>

<section class="customers">
  <h2 style="left:77px;top:292px">IDENTIFY YOUR CUSTOMERS</h2>
  <p class="abs lede" style="left:78px;top:320px">Do you REALLY know your customers?</p>
  <p class="abs copy" style="left:78px;top:344px;width:500px">Who are they? What are they looking for when wanting your service? What are their preferences in browsing device? What is making them leave your pages before they have read the content you want them to?</p>

  <div class="abs stat green"><div class="stat-label">LEAVE BEFORE 6<br>SECONDS</div><div class="stat-bar"><div class="stat-fill" style="width:85px"></div></div><div class="stat-pct">90%</div></div>
  <div class="abs stat rust"><div class="stat-label single">SEARCHWELL USERS</div><div class="stat-bar"><div class="stat-fill" style="width:66px"></div></div><div class="stat-pct">33%</div></div>
  <div class="abs stat navy"><div class="stat-label single">CIRCLEBOOK USERS</div><div class="stat-bar"><div class="stat-fill" style="width:66px"></div></div><div class="stat-pct">41%</div></div>
  <div class="abs stat sky"><div class="stat-label single">TABLET USERS</div><div class="stat-bar"><div class="stat-fill" style="width:27px"></div></div><div class="stat-pct">31%</div></div>

  <p class="abs stat-caption" style="left:88px;width:116px">Unless finding what they want, 90% of visitors will click off your page within 6 seconds!</p>
  <p class="abs stat-caption" style="left:222px;width:155px">33% use Searchwell Circles</p>
  <p class="abs stat-caption" style="left:390px">41% prefer Circlebook</p>
  <p class="abs stat-caption" style="left:539px;width:122px">31% of all users are using a tablet device</p>
</section>

<section class="metrics">
  <h2 style="left:78px;top:506px">DO YOU KNOW YOUR METRICS?</h2>
  <p class="abs copy" style="left:81px;top:533px">Do you know what content is converting your visitors or worse, which content is driving them away!</p>
  <p class="abs copy" style="left:81px;top:556px;width:512px">We work with you to develop strategies to identify this information, that allows you to optimise your content for your visitor's preferences.</p>
</section>

<section class="sells">
  <h2 style="left:78px;top:595px">CREATE CONTENT THAT SELLS</h2>
  <div class="abs video">
    <div class="video-art" role="img" aria-label="Numbered five-step SEO process wheel in peach tones"></div>
    <svg class="video-play" width="30" height="30" viewBox="0 0 30 30"><circle cx="15" cy="15" r="15" fill="#3a2a22" opacity=".85"/><path d="M12 9l9 6-9 6z" fill="#fff"/></svg>
  </div>
  <div class="abs copy sells-text">
    <p>We work with you, provide the tools and support that will allow you to create content on a regular basis that will sell you business to your customers.</p>
    <p style="margin-top:15px">The key to SEO in 2014 and beyond is CONTENT. Great, regular updated content. This is great, no longer is SEO a black art of tricking the search engines into returning your content by faking a whole lot of backlinks. Now it is all about providing valuable content to your customers, decreasing customer bounce rates, and in return</p>
  </div>
  <div class="abs btn-more">Read more</div>
</section>

<section class="plan">
  <div class="abs tab plan">WHATS THE PLAN?</div>
  <div class="abs tab packages">VIEW OUR PACKAGES</div>
  <div class="abs tab articles">STRATEGIC PLANNING<br>ARTICLES</div>
  <div class="abs tab-pointer"></div>

  <p class="abs plan-copy" style="top:887px">Day 1</p>
  <p class="abs plan-copy" style="top:909px">Half day meeting to analyse your current business, its customers and your current online presence.</p>
  <p class="abs plan-copy" style="top:932px">The purpose of this meeting is to allow us to determine the work required over the next 12 months to increase your exposure.</p>
  <p class="abs plan-copy" style="top:954px">It will look at the entire sales funnel, from who your customers are, what are hoping for when looking for your services, and what may be turning them away.</p>
  <p class="abs plan-copy" style="top:989px">Analyse your current website, SEO position, Social exposure and determine what we can do to improve the performance of these areas</p>
  <p class="abs plan-copy" style="top:1011px">If required, look at your lead tracking systems and streamline these to ensure that you capture, follow through and convert all possible leads. Burning a lead means you are losing multiple leads and sales due to loss of referral opportunities.</p>

  <div class="abs day active" style="left:71px;width:72px">Day 1</div>
  <div class="abs day" style="left:146px;width:72px">Day 1 - Day 14</div>
  <div class="abs day" style="left:222px;width:73px">Day 14</div>
  <div class="abs day" style="left:299px;width:92px">Day 14 - Month 12</div>
  <div class="abs day" style="left:396px;width:72px">Month 12</div>
</section>

<div class="share-row">
  <div class="abs share" style="left:86px"><span class="share-btn">Like</span><span class="share-btn">Share</span><span class="share-count">1</span></div>
  <div class="abs share" style="left:175px"><span class="share-btn">Chirp</span><span class="share-count">0</span></div>
  <div class="abs share" style="left:264px"><span class="share-btn">+1</span><span class="share-count">0</span></div>
  <div class="abs share" style="left:353px"><span class="share-btn">Pinlo</span></div>
  <div class="abs share" style="left:441px"><span class="share-dot"></span><span class="share-btn">Submit</span></div>
  <div class="abs share" style="left:531px"><span class="share-btn">Tumblo +</span></div>
  <div class="abs share" style="left:619px"><span class="share-btn">Share</span></div>
</div>

<footer>
  <nav class="abs footer-nav"><span>Home</span><span>Strategic Planning</span><span>SEO</span><span>Contact Us</span></nav>
  <p class="abs copyright">© 2014.www.companyname.com</p>
</footer>
<div class="rule-bottom"></div>
</body>
</html>
```